Business Card Design for Massage Therapist

*I am a qualified massage therapist & require a business card for my new business 'Tidal Touch & Wellness'.
*Contact details I'd like included on the card are: Elise Brantry, Mobile: 0481562930, Email: tidaltw@mailvane.com
*It is a massage business dedicated to providing quality therapeutic massage treatments, that will later incorporate natural therapies.
* Styles Include: Swedish, Relaxation, Pregnancy, Deep Tissue & Sports Massage
*I offer the styles of massage as listed above & a mobile service that allows clients to book a massage in the comfort of their own home.
*I'd like my logo to be fairly simple, streamlined, modern & reflect what my business services are - one people will easily remember.
*I'd like the colors to represent & emit a sense of calm, be fresh, welcoming, natural colors that appeal to a wide range of people.
*Colors I'd like to see are: pale blue, aqua & greens.

Target Market(s)

Both Male & Female, aged 20 to 65, singles, couples, parents, business people who are interested in their health, fitness & general wellbeing and maintenance. Located in the Harbourvale area and surrounding suburbs of Melbourne.

Industry/Entity Type

Massage

Requirements
Must have
• Fonts used in logos should be owned by the designer.
Should not have
• I don't want the design to have someone being massaged in it (pictures/photos) or have it look too clinical & sterile.

```html
<!DOCTYPE html>
<html lang="en">
<head>
<meta charset="utf-8">
<title>Tidal Touch &amp; Wellness — Business Card</title>
<link rel="stylesheet" href="https://fonts.googleapis.com/css2?family=Tinos&display=swap">
<style>
  :root {
    --paper: #ffffff;
    --ink: #1c1c1c;
    --edge: #222222;
    --band: #8fdfea;
    --band-text: #ffffff;
    --ring: #2ee86a;
    --frame: #b4f5dc;
  }
  * { margin: 0; padding: 0; box-sizing: border-box; }
  html, body { width: 827px; height: 1200px; overflow: hidden; background: var(--paper); }
  body { position: relative; font-family: "Tinos", "Times New Roman", serif; color: var(--ink); }

  .card { position: absolute; left: 36px; width: 748px; border: 1px solid var(--edge); background: var(--paper); }
  .card--front { top: 47px; height: 531px; }
  .card--back { top: 615px; height: 529px; }
  .card svg.decor { position: absolute; inset: 0; width: 100%; height: 100%; }

  .brand-band {
    position: absolute; background: var(--band); color: var(--band-text);
    white-space: nowrap; letter-spacing: 0.01em; line-height: 1;
    display: flex; align-items: center;
  }
  .card--front .brand-band { left: 44px; top: 188px; width: 476px; height: 48px; font-size: 28px; padding-left: 18px; }
  .card--back .brand-band { left: 399px; top: 46px; width: 225px; height: 23px; font-size: 12.5px; padding-left: 8px; }

  .name-band {
    position: absolute; left: 19px; top: 204px; width: 384px; height: 46px;
    background: var(--band); color: var(--band-text);
    font-size: 28px; line-height: 1; padding-left: 9px;
    display: flex; align-items: center; white-space: nowrap;
  }
  .role { position: absolute; left: 27px; top: 255px; font-size: 14px; }
  .services { position: absolute; left: 27px; top: 292px; list-style: none; font-size: 14px; line-height: 19.5px; }
  .contact { position: absolute; right: 21px; top: 471px; text-align: right; font-size: 15.5px; line-height: 19px; }
  .contact .email { font-size: 14.5px; }
</style>
</head>
<body>

  <section class="card card--front" aria-label="Card front">
    <svg class="decor" viewBox="0 0 748 531" aria-hidden="true">
      <rect class="frame" x="11" y="11" width="726" height="507" fill="none" stroke="var(--frame)" stroke-width="3"/>
      <circle class="logo-ring" cx="562" cy="273" r="159" fill="none" stroke="var(--ring)" stroke-width="2.5"/>
    </svg>
    <div class="brand-band">TIDAL TOUCH &amp; WELLNESS</div>
  </section>

  <section class="card card--back" aria-label="Card back">
    <svg class="decor" viewBox="0 0 748 529" aria-hidden="true">
      <line class="frame" x1="736" y1="9" x2="736" y2="516" stroke="var(--frame)" stroke-width="3"/>
      <line class="frame" x1="11" y1="516" x2="736" y2="516" stroke="var(--frame)" stroke-width="3"/>
      <circle class="logo-ring" cx="648" cy="91" r="77" fill="none" stroke="var(--ring)" stroke-width="1.5"/>
    </svg>
    <div class="brand-band">TIDAL TOUCH &amp; WELLNESS</div>

    <div class="name-band">ELISE BRANTRY</div>
    <p class="role">MASSAGE THERAPIST</p>
    <ul class="services">
      <li>SWEDISH</li>
      <li>RELAXATION</li>
      <li>PREGNANCY</li>
      <li>DEEP TISSUE</li>
      <li>SPORTS MASSAGE</li>
    </ul>
    <address class="contact" style="font-style: normal;">
      <div class="mobile">MOBILE: 0481 562 930</div>
      <div class="email">E-MAIL: tidaltw@mailvane.com</div>
    </address>
  </section>

</body>
</html>
```